Need business card design
Velin Medical
Simple
Tobias Morvel
CEO
12345 any street
city, state 98765
tmorvel@velinmedical.net
www.velinmedical.net
Just looking for design for now. Additional info will be added later

```html
<!DOCTYPE html>
<html lang="en">
<head>
<meta charset="utf-8">
<title>Velin Medical – Stationery Set</title>
<link rel="stylesheet" href="https://fonts.googleapis.com/css2?family=Poppins:wght@300;400;600&display=swap">
<style>
  :root{
    --board:#8a6a20;
    --paper:#ffffff;
    --ink:#151515;
    --green:#35a84a;
    --grey:#8d8d8d;
    --faint:#e6e6e6;
    --env-grey:#d9d9d9;
    --label:#2a2208;
  }
  *{box-sizing:border-box;margin:0;padding:0}
  html,body{width:1200px;height:540px;overflow:hidden}
  body{background:var(--board);font-family:"Poppins",sans-serif;color:var(--ink);position:relative}
  .sheet,.envelope,.card{position:absolute;background:var(--paper);box-shadow:0 2px 4px rgba(0,0,0,.35);overflow:hidden}

  /* wordmark: name in one colour and weight, with a plain square */
  .mark{position:absolute;display:flex;align-items:center;gap:.3em;font-weight:600;white-space:nowrap;line-height:1}
  .mark::before{content:"";width:.45em;height:.45em;background:var(--green);flex:none}
  .mark--dark{color:var(--ink)}
  .mark--light{color:var(--paper)}
  .mark--faint{color:var(--faint)}
  .mark--faint::before{background:var(--faint)}
  .mark--centered{left:50%;top:50%;transform:translate(-50%,-50%)}

  .tiny{position:absolute;font-size:4.5px;line-height:1.5;white-space:nowrap}
  .option-label{position:absolute;top:494px;font-size:20px;font-weight:300;color:var(--label);width:200px;text-align:center}

  /* letterhead */
  .letterhead{left:67px;top:48px;width:317px;height:425px}
  .letterhead .footer-rule{position:absolute;left:18px;right:18px;bottom:18px;height:2px;background:var(--green)}
  .letterhead .footer-text{left:18px;bottom:8px;color:var(--grey)}

  /* fax */
  .fax{left:408px;top:48px;width:324px;height:425px}
  .fax .head{position:absolute;left:0;top:0;width:100%;height:67px;background:var(--ink)}
  .fax .head .tiny{color:#cfcfcf;right:30px;top:12px;text-align:left}
  .fax .title{position:absolute;left:34px;top:100px;font-size:19px;font-weight:400;letter-spacing:1px}
  .fax .fields{position:absolute;left:34px;top:135px;width:264px;display:grid;grid-template-columns:1fr 1fr;column-gap:14px;row-gap:5px}
  .fax .field{font-size:5px;color:var(--grey);border-bottom:1px solid #9a9a9a;height:10px;line-height:8px}
  .fax .checks{position:absolute;left:34px;top:225px;display:flex;gap:10px}
  .fax .check{display:flex;align-items:center;gap:3px;font-size:5px;color:var(--grey)}
  .fax .check::before{content:"";width:7px;height:7px;border:1px solid #777}
  .fax .foot{position:absolute;left:0;bottom:0;width:100%;height:14px;background:var(--ink)}
  .fax .foot .tiny{color:#cfcfcf;left:130px;top:4px}

  /* envelopes */
  .envelope--black{background:var(--ink);left:768px;top:24px;width:168px;height:91px}
  .envelope--grey{background:var(--env-grey);left:876px;top:108px;width:192px;height:80px}
  .envelope--front{left:768px;top:166px;width:168px;height:92px}
  .envelope--back{left:876px;top:190px;width:192px;height:92px}
  .envelope--long{left:768px;top:242px;width:300px;height:82px}
  .flap{position:absolute;inset:0}
  .envelope .tiny{color:var(--grey)}

  /* business cards */
  .card{width:139px;height:79px}
  .card--black{background:var(--ink)}
  .card--a{left:768px;top:341px}
  .card--b{left:931px;top:341px}
  .card--c{left:768px;top:432px}
  .card--d{left:931px;top:432px}
  .card .panel{position:absolute;top:0;right:0;width:60%;height:100%;background:var(--ink)}
  .card .details{color:#d6d6d6}
  .card .details strong{font-weight:600;color:var(--paper)}
  .card .rule{position:absolute;left:0;bottom:0;width:100%;height:3px;background:var(--green)}
</style>
</head>
<body>

  <!-- Option 1: letterhead -->
  <section class="sheet letterhead">
    <div class="mark mark--dark" style="left:118px;top:14px;font-size:12px">Velin Medical</div>
    <div class="mark mark--faint" style="left:22px;top:125px;font-size:30px">Velin Medical</div>
    <div class="footer-rule"></div>
    <div class="tiny footer-text">12345 any street, city, state 98765 &nbsp;·&nbsp; tmorvel@velinmedical.net &nbsp;·&nbsp; www.velinmedical.net</div>
  </section>
  <div class="option-label" style="left:108px">option 1</div>

  <!-- Option 2: fax sheet -->
  <section class="sheet fax">
    <div class="head">
      <div class="mark mark--light" style="left:34px;top:20px;font-size:15px">Velin Medical</div>
      <div class="tiny">12345 any street<br>city, state 98765<br>tmorvel@velinmedical.net<br>www.velinmedical.net</div>
    </div>
    <div class="title">FAX</div>
    <div class="fields">
      <div class="field">To</div><div class="field">From</div>
      <div class="field">Fax</div><div class="field">Phone</div>
      <div class="field">Date</div><div class="field">Pages</div>
      <div class="field">Re</div><div class="field">CC</div>
    </div>
    <div class="checks">
      <span class="check">Urgent</span>
      <span class="check">For Review</span>
      <span class="check">Please Comment</span>
      <span class="check">Please Reply</span>
      <span class="check">Please Recycle</span>
    </div>
    <div class="mark mark--faint" style="right:16px;bottom:30px;font-size:16px">Velin Medical</div>
    <div class="foot"><div class="tiny">www.velinmedical.net</div></div>
  </section>
  <div class="option-label" style="left:455px">option 2</div>

  <!-- Envelopes -->
  <section class="envelope envelope--black">
    <div class="mark mark--light" style="left:14px;top:24px;font-size:13px">Velin Medical</div>
    <div class="tiny" style="left:14px;top:44px;color:#bdbdbd">12345 any street, city, state 98765</div>
  </section>

  <section class="envelope envelope--grey">
    <svg class="flap" viewBox="0 0 192 80" preserveAspectRatio="none" aria-hidden="true">
      <polygon points="0,0 192,0 96,40" fill="#c4c4c4"/>
    </svg>
    <div class="mark mark--dark" style="right:12px;top:8px;font-size:8px">Velin Medical</div>
  </section>

  <section class="envelope envelope--front">
    <div class="mark mark--dark" style="left:10px;top:10px;font-size:10px">Velin Medical</div>
    <div class="tiny" style="left:10px;top:24px">12345 any street<br>city, state 98765</div>
  </section>

  <section class="envelope envelope--back">
    <svg class="flap" viewBox="0 0 192 92" preserveAspectRatio="none" aria-hidden="true">
      <polyline points="0,0 96,44 192,0" fill="none" stroke="#d4d4d4" stroke-width="1"/>
    </svg>
    <div class="mark mark--dark" style="right:12px;top:8px;font-size:8px">Velin Medical</div>
  </section>

  <section class="envelope envelope--long">
    <div class="mark mark--dark" style="left:16px;top:12px;font-size:13px">Velin Medical</div>
    <div class="tiny" style="left:16px;top:30px">12345 any street, city, state 98765</div>
    <div style="position:absolute;left:0;bottom:0;width:100%;height:3px;background:var(--green)"></div>
    <div class="tiny" style="right:14px;bottom:8px">www.velinmedical.net</div>
  </section>

  <!-- Business cards -->
  <section class="card card--a">
    <div class="mark mark--dark" style="left:6px;top:33px;font-size:8px">Velin</div>
    <div class="panel">
      <div class="tiny details" style="left:8px;top:10px"><strong>Tobias Morvel</strong><br>CEO<br><br>12345 any street<br>city, state 98765<br>tmorvel@velinmedical.net</div>
    </div>
  </section>

  <section class="card card--b">
    <div class="mark mark--dark mark--centered" style="font-size:10px">Velin Medical</div>
  </section>

  <section class="card card--c card--black">
    <div class="tiny details" style="left:8px;top:10px"><strong>Tobias Morvel</strong><br>CEO<br>tmorvel@velinmedical.net<br>www.velinmedical.net</div>
    <div class="mark mark--light" style="left:8px;bottom:10px;font-size:8px">Velin Medical</div>
    <div class="rule"></div>
  </section>

  <section class="card card--d card--black">
    <div class="mark mark--light mark--centered" style="font-size:10px">Velin Medical</div>
  </section>

</body>
</html>
```